Steady Harbor- A Patient's Complete Guide to Navigating a Serious Illness

This is a book cover sall the aspects of managing a cancer diagnosis from what to do when you first get the diagnosis to magaing finances and lift after cancer.

Successful candidate will familarize themselves with the elements of the book and incorporate the elements into the main graphic which is a fist punching down from above crushing the word cancer.

I have "Steady" Harbor, it shoudl be Crushing.

Also, the word crushing may be above then the fist coming down on the word cancer.

```html
<!DOCTYPE html>
<html lang="en">
<head>
<meta charset="utf-8">
<title>Steady Harbor – Wraparound Cover</title>
<link href="https://fonts.googleapis.com/css2?family=Anton&family=Roboto+Condensed:wght@400;500&family=Open+Sans:wght@400&display=swap" rel="stylesheet">
<style>
  :root {
    --page: #ffffff;
    --navy-deep: #0f0c3f;
    --navy: #1c1866;
    --cell-glow: #34287a;
    --cell-red: #4e1d4e;
    --white: #ffffff;
    --red: #d8141c;
    --skin-light: #d2a48c;
    --skin-mid: #b07a60;
    --skin-dark: #7a4a33;
  }
  * { margin: 0; padding: 0; box-sizing: border-box; }
  html, body {
    width: 786px; height: 1200px; overflow: hidden;
    background: var(--page);
  }
  .wrap {
    position: absolute; left: 0; top: 315px;
    width: 786px; height: 570px; overflow: hidden;
    background: var(--navy-deep);
  }
  .wrap-backdrop {
    position: absolute; inset: 0;
    background:
      radial-gradient(ellipse 30% 35% at 75% 40%, var(--cell-red) 0%, transparent 70%),
      radial-gradient(ellipse 25% 30% at 62% 70%, var(--cell-glow) 0%, transparent 70%),
      radial-gradient(ellipse 25% 30% at 92% 15%, var(--cell-glow) 0%, transparent 70%),
      linear-gradient(90deg, var(--navy-deep) 0%, var(--navy-deep) 47%, var(--navy) 60%, var(--navy) 100%);
  }

  /* back panel */
  .back { position: absolute; left: 0; top: 0; width: 367px; height: 570px; }
  .back-copy {
    position: absolute; left: 46px; top: 86px; width: 288px;
    color: var(--white); font-family: 'Open Sans', sans-serif;
    font-size: 10.2px; line-height: 15.7px; text-align: justify;
    letter-spacing: -0.2px;
  }
  .back-copy p + p { margin-top: 15.7px; }

  /* spine */
  .spine { position: absolute; left: 367px; top: 0; width: 52px; height: 570px; }
  .spine-title {
    position: absolute; left: 50%; top: 175px; transform: translateX(-50%);
    writing-mode: vertical-rl; font-family: 'Anton', sans-serif;
    font-size: 20px; line-height: 1; text-transform: uppercase; letter-spacing: 0.5px;
  }
  .spine-title .top { color: var(--white); }
  .spine-title .bottom { color: var(--red); margin-top: 6px; }
  .spine-author {
    position: absolute; left: 50%; top: 420px; transform: translateX(-50%);
    writing-mode: vertical-rl; color: var(--white);
    font-family: 'Roboto Condensed', sans-serif; font-weight: 500;
    font-size: 9.5px; text-transform: uppercase; letter-spacing: 0.4px;
  }

  /* front panel */
  .front { position: absolute; left: 419px; top: 0; width: 367px; height: 570px; }
  .fist { position: absolute; }
  .fist-top {
    left: 141px; top: 0; width: 79px; height: 149px;
    border-radius: 10px 10px 30px 30px / 10px 10px 40px 40px;
    background: linear-gradient(180deg, var(--skin-dark) 0%, var(--skin-mid) 55%, var(--skin-light) 100%);
  }
  .fist-left {
    left: -13px; top: 181px; width: 85px; height: 98px;
    border-radius: 20px 46px 46px 20px;
    background: linear-gradient(90deg, var(--skin-light) 0%, #e3c3b0 50%, var(--skin-mid) 100%);
  }
  .fist-right {
    left: 272px; top: 188px; width: 95px; height: 98px;
    border-radius: 46px 10px 10px 46px;
    background: linear-gradient(270deg, var(--skin-mid) 0%, var(--skin-light) 60%, #c8967c 100%);
  }
  .title {
    position: absolute; left: 40px; top: 128px; width: 290px;
    text-align: center; font-family: 'Anton', sans-serif; font-weight: 400;
    text-transform: uppercase; line-height: 1;
  }
  .title-top {
    display: block; color: var(--white); font-size: 96px; line-height: 88px;
    transform: scaleX(0.86);
  }
  .title-bottom {
    display: block; color: var(--red); font-size: 96px; line-height: 86px;
    transform: scaleX(0.92);
  }
  .subtitle {
    position: absolute; left: 0; width: 354px; top: 352px;
    text-align: center; color: var(--white);
    font-family: 'Roboto Condensed', sans-serif; font-weight: 400;
    font-size: 22px; line-height: 30px;
  }
  .author {
    position: absolute; left: 0; width: 354px; top: 508px;
    text-align: center; color: var(--white);
    font-family: 'Roboto Condensed', sans-serif; font-weight: 500;
    font-size: 25px; line-height: 30px; text-transform: uppercase;
  }
</style>
</head>
<body>
  <main class="wrap">
    <div class="wrap-backdrop" role="img" aria-label="Dark navy microscopic cell texture with faint molecular structure diagrams"></div>

    <section class="back">
      <div class="back-copy">
        <p>Lorem ipsum dolor sit amet, consectetur adipiscing elit. Pellentesque elementum purus pulvinar euismod hendrerit. Mauris ac risus tristique, condimentum massa in, hendrerit nulla. Quisque pulvinar sagittis leo, in ultrices massa hendrerit eget. Quisque ac imperdiet nulla. Etiam tortor felis, tincidunt ac auctor et, euismod sed arcu. Mauris risus mauris, consectetur sed nisi et, commodo tincidunt urna. Pellentesque porta, dui quis mollis sollicitudin, justo est consequat augue, sit amet elementum nisl quam maximus massa. Vestibulum tincidunt mauris interdum ipsum egestas lobortis.</p>
        <p>Maecenas ut nisl nec tortor pretium ultricies. Vestibulum blandit, erat eu ornare lobortis, est orci dictum augue, at commodo purus augue rhoncus augue. Suspendisse egestas felis lorem, ut vestibulum est porttitor et. Nam tempus, dolor vel placerat auctor, ex tellus laoreet lorem, non vestibulum elit nisl quis nisl.</p>
        <p>Maecenas suscipit quis quam non auctor. Aenean sed fermentum orci. Etiam sit amet lorem velit. Etiam feugiat sapien a fermentum semper. Etiam maximus condimentum lectus sed sodales. Nunc auctor erat non erat consectetur commodo. Sed in semper nulla. In tincidunt, diam sed gravida facilisis, neque mauris cursus ante, eget finibus elit purus in dolor.</p>
      </div>
    </section>

    <section class="spine">
      <p class="spine-title"><span class="top">Steady</span> <span class="bottom">Harbor</span></p>
      <p class="spine-author">Dana M. Whitlow MD</p>
    </section>

    <section class="front">
      <div class="fist fist-top" role="img" aria-label="Photo of a fist punching down from above onto the title"></div>
      <div class="fist fist-left" role="img" aria-label="Photo of a fist pressing in from the left"></div>
      <div class="fist fist-right" role="img" aria-label="Photo of a fist pressing in from the right"></div>

      <h1 class="title">
        <span class="title-top">Steady</span>
        <span class="title-bottom">Harbor</span>
      </h1>

      <p class="subtitle">A Patient's Complete Guide<br>to Navigating a Serious Illness</p>
      <p class="author">Dana M. Whitlow MD</p>
    </section>
  </main>
</body>
</html>
```